My business is Property developing Stationary

I want business card and stationery. Please have the formate so I can edit details on card and stationary.

Please see my logo and on the back of the card I want it same red as my logo and I will provide copy that I want on the back of the card.

Also need an email signature

On the business card and email signature add below copy:
Project Management- Acquisitions- Syndicates- Joint Ventures

Target Market(s)

Property investors

Industry/Entity Type

Business

Requirements
Must have
• Reflect my Logo

```html
<!DOCTYPE html>
<html lang="en">
<head>
<meta charset="utf-8">
<title>Harborne Property Developments – Business Card</title>
<link rel="stylesheet" href="https://fonts.googleapis.com/css2?family=Montserrat:wght@600;700&family=Questrial&display=swap">
<style>
  :root {
    --brand-red: #d4372a;
    --ink: #1b1b1b;
    --text-grey: #333333;
    --paper: #ffffff;
    --page-bg: #e9e8ec;
    --ghost: #eceef1;
    --ghost-deep: #e3e5e9;
  }
  * { box-sizing: border-box; margin: 0; padding: 0; }
  html, body { width: 1200px; height: 934px; overflow: hidden; }
  body {
    background: var(--page-bg);
    font-family: "Questrial", "Helvetica Neue", Arial, sans-serif;
    position: relative;
  }
  .card {
    position: absolute;
    left: 250px;
    width: 700px;
    height: 400px;
    overflow: hidden;
    box-shadow: 0 6px 18px rgba(0,0,0,0.12);
  }
  .card-back { top: 45px; background: var(--brand-red); }
  .card-front { top: 489px; background: var(--paper); }
  .card-art { position: absolute; inset: 0; width: 700px; height: 400px; }

  .wordmark {
    position: absolute;
    font-family: "Montserrat", "Helvetica Neue", Arial, sans-serif;
    font-weight: 700;
    letter-spacing: 2px;
    line-height: 1;
  }
  .wordmark-tagline {
    position: absolute;
    font-family: "Montserrat", "Helvetica Neue", Arial, sans-serif;
    font-weight: 600;
    line-height: 1;
  }
  .card-back .wordmark { left: 345px; top: 92px; font-size: 52px; color: var(--paper); }
  .card-back .wordmark-tagline { left: 378px; top: 150px; font-size: 15px; color: var(--paper); }
  .card-back .web-address {
    position: absolute; right: 48px; bottom: 44px;
    font-size: 14px; color: var(--paper); letter-spacing: 0.5px;
  }

  .card-front .wordmark { left: 48px; top: 120px; font-size: 52px; color: var(--brand-red); }
  .card-front .wordmark-tagline { left: 80px; top: 178px; font-size: 15px; color: var(--ink); }

  .person { position: absolute; right: 56px; top: 40px; text-align: right; }
  .person-name {
    font-family: "Montserrat", "Helvetica Neue", Arial, sans-serif;
    font-weight: 700; font-size: 20px; letter-spacing: 0.5px;
    color: var(--brand-red);
  }
  .person-title { font-size: 16px; color: var(--ink); margin-top: 4px; }

  .contact-list { position: absolute; left: 60px; top: 240px; list-style: none; }
  .contact-item {
    display: flex; align-items: center; gap: 10px;
    font-size: 16px; color: var(--text-grey); height: 24px;
  }
  .contact-icon { width: 17px; height: 17px; flex: none; }
  .address { position: absolute; left: 60px; top: 322px; font-size: 16px; line-height: 22px; color: var(--text-grey); }
</style>
</head>
<body>

<section class="card card-back" aria-label="Business card, back">
  <svg class="card-art" viewBox="0 0 700 400" aria-hidden="true">
    <polygon points="0,205 352,400 0,400" fill="var(--paper)"/>
    <polygon points="0,240 290,400 0,400" fill="var(--ink)"/>
    <polygon points="0,272 232,400 0,400" fill="var(--paper)"/>
    <polygon points="0,306 170,400 0,400" fill="var(--brand-red)"/>
  </svg>
  <div class="wordmark">HARBORNE</div>
  <div class="wordmark-tagline">Property Developments</div>
  <div class="web-address">www.harborne-dev.com</div>
</section>

<section class="card card-front" aria-label="Business card, front">
  <svg class="card-art" viewBox="0 0 700 400" aria-hidden="true">
    <polygon points="520,384 660,120 700,120 700,140 575,384" fill="var(--ghost)"/>
    <polygon points="570,384 680,190 700,190 700,215 610,384" fill="var(--ghost-deep)"/>
    <polygon points="596,384 700,268 700,298 628,384" fill="var(--ink)"/>
    <polygon points="0,384 640,384 700,320 700,400 0,400" fill="var(--brand-red)"/>
  </svg>

  <div class="wordmark">HARBORNE</div>
  <div class="wordmark-tagline">Property Developments</div>

  <div class="person">
    <div class="person-name">SAM WHITFIELD</div>
    <div class="person-title">Managing Director</div>
  </div>

  <ul class="contact-list">
    <li class="contact-item">
      <svg class="contact-icon" viewBox="0 0 16 16" aria-hidden="true">
        <rect width="16" height="16" rx="3" fill="var(--brand-red)"/>
        <path d="M5 3.5 L7 5.5 L6 7 Q7 9 9 10 L10.5 9 L12.5 11 L11 12.5 Q7 12.5 3.5 5 Z" fill="var(--paper)"/>
      </svg>
      1300 555 012
    </li>
    <li class="contact-item">
      <svg class="contact-icon" viewBox="0 0 16 16" aria-hidden="true">
        <rect width="16" height="16" rx="3" fill="var(--brand-red)"/>
        <rect x="3" y="4.5" width="10" height="7" fill="none" stroke="var(--paper)" stroke-width="1.3"/>
        <path d="M3 4.5 L8 8.5 L13 4.5" fill="none" stroke="var(--paper)" stroke-width="1.3"/>
      </svg>
      info@harborne-dev.com
    </li>
    <li class="contact-item">
      <svg class="contact-icon" viewBox="0 0 16 16" aria-hidden="true">
        <rect width="16" height="16" rx="3" fill="var(--brand-red)"/>
        <circle cx="8" cy="8" r="4.8" fill="none" stroke="var(--paper)" stroke-width="1.2"/>
        <ellipse cx="8" cy="8" rx="2" ry="4.8" fill="none" stroke="var(--paper)" stroke-width="1"/>
        <line x1="3.2" y1="8" x2="12.8" y2="8" stroke="var(--paper)" stroke-width="1"/>
      </svg>
      www.harborne-dev.com
    </li>
  </ul>

  <address class="address" style="font-style: normal;">
    Level 12, Kestrel House<br>
    18 Wharf Lane, Sydney
  </address>
</section>

</body>
</html>
```